Tech Startup Needs Business Card Design

I am looking for an eye catching business card design for our new company, Torn Kite. We are a place for business owners and contractors to share their experiences with their customers and check their current customers. Our website, www.torn-kite.co, may be able to offer some guidance as to the design.

Industry/Entity Type

Business

Contact Information for Business Card

Owen Barthwick
888-417-3083
Owen@torn-kite.co
www.torn-kite.co

```html
<!DOCTYPE html>
<html lang="en">
<head>
<meta charset="utf-8">
<title>Torn Kite — Business Card</title>
<link href="https://fonts.googleapis.com/css2?family=Noto+Sans:wght@400;700&display=swap" rel="stylesheet">
<style>
  :root {
    --backdrop: #3a3a3c;
    --card: #1f2022;
    --brand-red: #e0312b;
    --ink-light: #f2f2f2;
    --rule: #d9d9d9;
  }
  * { box-sizing: border-box; margin: 0; padding: 0; }
  html, body {
    width: 1200px; height: 1189px; overflow: hidden;
    background: var(--backdrop);
    font-family: "Noto Sans", Verdana, sans-serif;
  }
  .sheet {
    position: relative; width: 1200px; height: 1189px;
    display: flex; flex-direction: column; align-items: center; justify-content: center; gap: 60px;
  }
  .card {
    position: relative; width: 880px; height: 480px;
    background: var(--card); border-radius: 24px;
    box-shadow: 0 14px 40px rgba(0,0,0,.45);
    overflow: hidden;
  }
  /* Front */
  .card--front { display: flex; align-items: center; justify-content: center; }
  .brand { display: flex; align-items: center; gap: 26px; }
  .brand__dot { width: 74px; height: 74px; border-radius: 50%; background: var(--brand-red); }
  .brand__name { font-size: 96px; font-weight: 700; color: var(--ink-light); letter-spacing: 1px; }

  /* Back */
  .card--back { display: flex; align-items: center; }
  .back__mark {
    width: 380px; height: 100%;
    display: flex; flex-direction: column; align-items: center; justify-content: center; gap: 22px;
  }
  .back__dot { width: 170px; height: 170px; border-radius: 50%; background: var(--brand-red); }
  .back__name { font-size: 34px; font-weight: 700; color: var(--ink-light); }
  .back__rule { width: 2px; height: 240px; background: var(--rule); opacity: .8; }
  .contact { padding-left: 56px; color: var(--ink-light); }
  .contact__name { font-size: 30px; font-weight: 700; color: var(--brand-red); margin-bottom: 30px; }
  .contact__address { font-size: 21px; line-height: 1.3; margin-bottom: 24px; }
  .contact__line { display: flex; align-items: center; gap: 12px; font-size: 22px; line-height: 1.5; }
  .contact__icon {
    width: 26px; height: 24px; border-radius: 4px; background: var(--brand-red);
    display: flex; align-items: center; justify-content: center;
  }
  .contact__web { font-size: 24px; color: var(--brand-red); margin-top: 14px; }
</style>
</head>
<body>
<main class="sheet">
  <section class="card card--front" aria-label="Card front">
    <div class="brand">
      <span class="brand__dot"></span>
      <span class="brand__name">Torn Kite</span>
    </div>
  </section>

  <section class="card card--back" aria-label="Card back">
    <div class="back__mark">
      <span class="back__dot"></span>
      <span class="back__name">Torn Kite</span>
    </div>
    <div class="back__rule"></div>
    <div class="contact">
      <p class="contact__name">Owen Barthwick</p>
      <p class="contact__address">your address,2nd street<br>Harlow Bend East. USA</p>
      <p class="contact__line">
        <span class="contact__icon">
          <svg width="16" height="16" viewBox="0 0 24 24" aria-hidden="true"><path fill="#fff" d="M6.6 10.8a15.1 15.1 0 0 0 6.6 6.6l2.2-2.2c.3-.3.7-.4 1-.2 1.1.4 2.3.6 3.6.6.6 0 1 .4 1 1V20c0 .6-.4 1-1 1A17 17 0 0 1 3 4c0-.6.4-1 1-1h3.5c.6 0 1 .4 1 1 0 1.3.2 2.5.6 3.6.1.3 0 .7-.2 1z"/></svg>
        </span>
        888-417-3083
      </p>
      <p class="contact__line">
        <span class="contact__icon">
          <svg width="18" height="14" viewBox="0 0 24 18" aria-hidden="true"><rect x="1.5" y="1.5" width="21" height="15" fill="none" stroke="#fff" stroke-width="2"/><path d="M1.5 1.5 12 10l10.5-8.5" fill="none" stroke="#fff" stroke-width="2"/></svg>
        </span>
        Owen@torn-kite.co
      </p>
      <p class="contact__web">torn-kite.co</p>
    </div>
  </section>
</main>
</body>
</html>
```